The Shelf Sage needs a pricing flyer

Single page flyer for the Shelf Sage.
The Shelf Sage is a lead generation service exclusively for the custom closet industry.
You design quality closets we provide quality leads!
Value Points:
Leads for closet companies are exclusive with a first right of refusal. Meaning, if the closet company cannot handle all of the leads we can provide, we will sell the excess to other closet companies. We will never sell the same lead to two different closet companies.
Benefits:
Flat rate and easy to budget
Cancel at anytime
Choose from 3 types of leads
Lower cost compared to overall cost per lead from other sources
More leads allows hiring more designers
More leads grow the companies revenue
Less time managing other advertising models
3 service options.
$250 each
- We send you the lead
- You and your team set the appointment
- Setting the appointment is up to you
2. $275 each
- We send you the lead
- We guarantee the appointment
- Return unset appointments for a replacement
3. $375 each
- We are your call center
- We generate the lead
- We set the appointment
Contact:
The Shelf Sage
704-555-0183
leads@TheShelfSage.example

```html
<!DOCTYPE html>
<html lang="en">
<head>
<meta charset="utf-8">
<title>The Shelf Sage – Pricing Flyer</title>
<link rel="stylesheet" href="https://fonts.googleapis.com/css2?family=Alfa+Slab+One&family=Open+Sans:ital,wght@0,400;0,600;0,700;1,400;1,600;1,700&display=swap">
<style>
  :root{
    --page:#ffffff;
    --mocha:#8a6a52;
    --mocha-deep:#765640;
    --band-dark:#6a4a36;
    --espresso:#2e1c14;
    --cream:#efe4d9;
    --panel-head:rgba(52,30,20,.88);
    --panel-body:rgba(140,105,80,.78);
    --price-strip:rgba(78,52,38,.95);
    --white:#ffffff;
  }
  *{margin:0;padding:0;box-sizing:border-box}
  html,body{width:1132px;height:1200px;overflow:hidden;background:var(--page)}
  body{position:relative;font-family:"Open Sans",sans-serif}
  .flyer{position:absolute;left:258px;top:168px;width:617px;height:865px;overflow:hidden;background:var(--mocha)}
  .flyer-shapes{position:absolute;inset:0;width:617px;height:865px}

  .brand-badge{position:absolute;left:203px;top:31px;width:210px;height:107px;border-radius:105px 105px 0 0;background:var(--cream);display:flex;align-items:flex-end;justify-content:center;padding-bottom:22px}
  .brand-name{font-family:"Open Sans",sans-serif;font-weight:600;font-size:21px;color:#6b4a35;white-space:nowrap}

  .contact{position:absolute;left:424px;top:28px;width:165px;height:80px;background:var(--mocha-deep);color:var(--white);padding:8px 0 0 10px}
  .contact-title{font-weight:700;font-style:italic;font-size:18px;line-height:22px}
  .contact-phone{display:flex;align-items:center;gap:7px;font-weight:600;font-style:italic;font-size:17px;line-height:24px;margin-top:1px}
  .contact-phone svg{width:20px;height:20px;flex:none}
  .contact-email{font-size:11.4px;line-height:16px;margin-top:1px}

  .headline{position:absolute;left:38px;top:154px;font-family:"Alfa Slab One",serif;color:var(--espresso);line-height:1}
  .headline span{display:block}
  .hl-small{font-size:22px;letter-spacing:.5px}
  .hl-big{font-size:36px;letter-spacing:.5px}
  .hl-mid{font-size:21px;letter-spacing:1px}
  .gap{margin-top:12px}

  .value-quote{position:absolute;left:40px;top:349px;width:262px;font-style:italic;font-size:13.2px;line-height:18.1px;color:var(--espresso);text-align:justify}
  .value-quote .mark{font-family:"Alfa Slab One",serif;font-style:normal;font-size:18px;line-height:10px;margin-right:2px}

  .panel-head{position:absolute;height:33px;background:var(--panel-head);color:var(--white);font-weight:700;font-size:17.5px;line-height:33px}
  .why-head{left:40px;top:561px;width:252px;padding-left:36px}
  .why-body{position:absolute;left:40px;top:594px;width:252px;height:238px;background:var(--panel-body);padding:6px 8px 0 28px}
  .benefits{list-style:none;color:var(--white);font-size:14.6px;line-height:18.2px}
  .benefits li{position:relative;margin-bottom:2.5px}
  .benefits li::before{content:"";position:absolute;left:-14px;top:7px;width:5px;height:5px;border-radius:50%;background:var(--white)}

  .pkg-head{left:325px;top:561px;width:253px;padding-left:29px}
  .pkg{position:absolute;left:325px;width:253px;background:var(--panel-body);display:flex}
  .pkg-1{top:594px;height:65px}
  .pkg-2{top:665px;height:95px}
  .pkg-3{top:766px;height:66px}
  .price{width:31px;flex:none;background:var(--price-strip);position:relative}
  .price span{position:absolute;left:50%;top:50%;transform:translate(-50%,-50%) rotate(-90deg);color:var(--white);font-weight:700;font-size:19px;white-space:nowrap}
  .pkg-points{list-style:none;color:var(--white);font-size:11.6px;line-height:16.4px;padding:4px 4px 0 15px}
  .pkg-points li{position:relative}
  .pkg-points li::before{content:"";position:absolute;left:-9px;top:6px;width:4px;height:4px;border-radius:50%;background:var(--white)}
</style>
</head>
<body>
<main class="flyer">
  <svg class="flyer-shapes" viewBox="0 0 1022 1433" preserveAspectRatio="none" aria-hidden="false">
    <defs>
      <linearGradient id="heroTone" x1="0" y1="0" x2="1" y2="0">
        <stop offset="0" stop-color="#a4856d"/>
        <stop offset=".55" stop-color="#c8b4a4"/>
        <stop offset="1" stop-color="#ddd0c6"/>
      </linearGradient>
      <linearGradient id="roomTone" x1="0" y1="0" x2="1" y2="1">
        <stop offset="0" stop-color="#4c3326"/>
        <stop offset=".5" stop-color="#6e5444"/>
        <stop offset="1" stop-color="#3b271d"/>
      </linearGradient>
    </defs>
    <rect x="0" y="0" width="1022" height="229" fill="var(--mocha)"/>
    <rect x="0" y="229" width="1022" height="571" fill="url(#heroTone)" role="img" aria-label="Sketch of a walk-in closet with shelves, hanging clothes and shoes, drawn by a hand holding a pencil"/>
    <rect x="0" y="800" width="1022" height="633" fill="url(#roomTone)" role="img" aria-label="Photo of a dark wood walk-in closet interior"/>
    <path d="M0,790 L0,1050 C20,930 90,880 180,880 L640,890 C820,895 960,850 1022,760 L1022,660 C980,760 900,800 780,810 L180,838 C90,840 30,820 0,790 Z" fill="var(--mocha)"/>
    <path d="M0,1060 C30,950 100,905 190,905 L640,912 C820,915 960,875 1022,800 L1022,775 C960,860 820,890 640,888 L180,882 C90,882 20,940 0,1050 Z" fill="var(--band-dark)"/>
  </svg>

  <div class="brand-badge"><span class="brand-name">The Shelf Sage</span></div>

  <aside class="contact">
    <p class="contact-title">Contact us:</p>
    <p class="contact-phone">
      <svg viewBox="0 0 20 20"><circle cx="10" cy="10" r="9" fill="none" stroke="#fff" stroke-width="1.3"/><path d="M6.5 5.5c.6-.5 1.3-.4 1.6.2l.8 1.6c.2.5 0 1-.4 1.3l-.5.4c.5 1.1 1.4 2 2.5 2.5l.4-.5c.3-.4.8-.6 1.3-.4l1.6.8c.6.3.7 1 .2 1.6-.8.9-2 1.3-3.2.8-2.2-.9-3.9-2.6-4.8-4.8-.5-1.2-.1-2.4.5-3.5z" fill="#fff"/></svg>
      704-555-0183
    </p>
    <p class="contact-email">leads@TheShelfSage.example</p>
  </aside>

  <h1 class="headline">
    <span class="hl-small">YOU</span>
    <span class="hl-big">DESIGN</span>
    <span class="hl-mid">QUALITY CLOSETS</span>
    <span class="hl-small gap">WE</span>
    <span class="hl-big">PROVIDE</span>
    <span class="hl-mid">QUALITY LEADS!</span>
  </h1>

  <p class="value-quote"><span class="mark">“</span>Leads for closet companies are exclusive with a first right of refusal. Meaning, if the closet company cannot handle all of the leads we can provide, we will sell the excess to other closet companies. We will never sell the same lead to two different closet companies.</p>

  <h2 class="panel-head why-head">Why Choose us ?</h2>
  <div class="why-body">
    <ul class="benefits">
      <li>Flat rate and easy to budget</li>
      <li>Cancel at anytime</li>
      <li>Choose from 3 types of leads</li>
      <li>Lower cost compared to overall cost per lead from other sources</li>
      <li>More leads allows hiring more designers</li>
      <li>More leads grow the companies revenue</li>
      <li>Less time managing other advertising models</li>
    </ul>
  </div>

  <h2 class="panel-head pkg-head">Packages</h2>
  <section class="pkg pkg-1">
    <div class="price"><span>$250</span></div>
    <ul class="pkg-points">
      <li>We send you the lead</li>
      <li>You and your team set the appointment</li>
      <li>Setting the appointment is up to you</li>
    </ul>
  </section>
  <section class="pkg pkg-2">
    <div class="price"><span>$275</span></div>
    <ul class="pkg-points">
      <li>We send you the lead</li>
      <li>You and your team set the appointment</li>
      <li>We guarantee the appointment</li>
      <li>Return unset appointments for a replacement</li>
    </ul>
  </section>
  <section class="pkg pkg-3">
    <div class="price"><span>$375</span></div>
    <ul class="pkg-points">
      <li>We are your call center</li>
      <li>We generate the lead</li>
      <li>We set the appointment</li>
    </ul>
  </section>
</main>
</body>
</html>
```